flyer for roofing advertising

Need a modern, bold, luxurious advertisement flyer for our roofing company. located in buffalo, ny. Big house with a intense roof design asphalt shingles. slogan is "Reliability starts at the top". Colors varies but want it to be modern. we will be handing these out when we are working in the area. phone number is 716-555-0147 for the NO K.W estimate. also our services are roofing, roof repairs, gutters, attic ventilation. we offer a 15 year warranty with our platinum roof program. We are certified by dwellmatch, harlan trevisk, quarno. Also follow us on linkpage, wexora and frunt. website is ktw-roofing.com, linkpage is ktwroofing. pictures are on linkpage and our website if need more can be provided. also can include a review we have.

```html
<!DOCTYPE html>
<html lang="en">
<head>
<meta charset="utf-8">
<title>KTW Roofing – Flyer and Business Cards</title>
<link rel="stylesheet" href="https://fonts.googleapis.com/css2?family=Anton&family=Montserrat:wght@800&family=Source+Sans+3:wght@400;600;700&family=Orbitron:wght@500;700&display=swap">
<style>
  :root {
    --orange: #f28c1c;
    --orange-deep: #e8780a;
    --black: #000;
    --white: #fff;
    --stage: #4b4b4b;
    --panel-top: #5a5a5a;
    --panel-bottom: #262626;
    --mark-gray: #8a8a8a;
  }
  html, body {
    margin: 0;
    width: 1200px;
    height: 1200px;
    overflow: hidden;
    background: var(--stage);
  }
  .stage { position: relative; width: 1200px; height: 1200px; }
  .piece { position: absolute; display: block; box-shadow: 0 4px 12px rgba(0,0,0,.35); }
  .flyer { left: 379px; top: 121px; width: 443px; height: 622px; }
  .card-front { left: 143px; top: 824px; width: 434px; height: 248px; }
  .card-back { left: 624px; top: 824px; width: 434px; height: 248px; }
  .body-text { font-family: "Source Sans 3", sans-serif; }
  .display { font-family: "Anton", sans-serif; }
  .heavy { font-family: "Montserrat", sans-serif; font-weight: 800; }
  .brand { font-family: "Source Sans 3", sans-serif; font-weight: 700; }
  .tagline { font-family: "Orbitron", sans-serif; font-weight: 500; }
</style>
</head>
<body>
<main class="stage">

  <!-- Flyer -->
  <svg class="piece flyer" viewBox="0 0 553 777" xmlns="http://www.w3.org/2000/svg">
    <defs>
      <linearGradient id="houseTones" x1="0" y1="0" x2="0" y2="1">
        <stop offset="0" stop-color="#c9c9cb"/>
        <stop offset="0.35" stop-color="#8a7a6a"/>
        <stop offset="0.7" stop-color="#5b4a3a"/>
        <stop offset="1" stop-color="#7d7a3a"/>
      </linearGradient>
      <linearGradient id="servicePanel" x1="0" y1="0" x2="0" y2="1">
        <stop offset="0" stop-color="var(--panel-top)"/>
        <stop offset="1" stop-color="var(--panel-bottom)"/>
      </linearGradient>
      <linearGradient id="orangeField" x1="0" y1="0" x2="1" y2="1">
        <stop offset="0" stop-color="var(--orange)"/>
        <stop offset="1" stop-color="var(--orange-deep)"/>
      </linearGradient>
    </defs>

    <rect class="hero-photo" width="553" height="400" fill="url(#houseTones)" role="img" aria-label="Photo of a large brick Tudor-style house with a dark asphalt shingle roof, autumn lawn and evergreen shrubs"/>

    <g class="top-chevron">
      <polygon points="240,0 525,0 393,62" fill="var(--black)"/>
      <polygon points="272,0 495,0 393,48" fill="var(--white)"/>
      <polygon points="302,0 468,0 393,36" fill="var(--orange)"/>
    </g>

    <g class="brand-block">
      <rect x="56" y="62" width="16" height="16" fill="var(--orange)"/>
      <text class="brand" x="80" y="84" font-size="34" fill="var(--mark-gray)">KTW</text>
      <text class="tagline" x="20" y="107" font-size="11.5" fill="var(--orange)">ROOFING-SIDING-STONE</text>
    </g>

    <g class="lower-band">
      <polygon points="0,372 230,318 302,300 553,372 553,725 0,725" fill="url(#orangeField)"/>
      <polygon points="230,306 302,287 553,358 553,372 302,300 230,318" fill="var(--black)"/>
      <polygon points="230,318 302,300 553,372 553,382 302,312 230,330" fill="var(--white)"/>
    </g>

    <g class="services-panel">
      <polygon points="20,322 230,270 230,603 20,603" fill="url(#servicePanel)"/>
      <circle cx="42" cy="339" r="8" fill="none" stroke="var(--orange)" stroke-width="1.5"/>
      <path d="M38 335 L46 343 M46 335 L38 343" stroke="var(--orange)" stroke-width="1.5"/>
      <text class="heavy" x="55" y="346" font-size="19" fill="var(--orange)" text-decoration="underline">OUR SERVICES</text>
      <g class="service-list body-text" font-size="13" font-weight="600" fill="var(--white)">
        <g transform="translate(0,368)"><circle cx="38" cy="-4" r="4.5" fill="var(--orange)"/><text x="48" y="0">Roof Installation</text></g>
        <g transform="translate(0,388)"><circle cx="38" cy="-4" r="4.5" fill="var(--orange)"/><text x="48" y="0">Roof Repair</text></g>
        <g transform="translate(0,408)"><circle cx="38" cy="-4" r="4.5" fill="var(--orange)"/><text x="48" y="0">Re-Roof</text></g>
        <g transform="translate(0,428)"><circle cx="38" cy="-4" r="4.5" fill="var(--orange)"/><text x="48" y="0">Commercial Roofing</text></g>
        <g transform="translate(0,448)"><circle cx="38" cy="-4" r="4.5" fill="var(--orange)"/><text x="48" y="0">Roof Inspection</text></g>
        <g transform="translate(0,468)"><circle cx="38" cy="-4" r="4.5" fill="var(--orange)"/><text x="48" y="0">Siding Repair</text></g>
        <g transform="translate(0,488)"><circle cx="38" cy="-4" r="4.5" fill="var(--orange)"/><text x="48" y="0">New Siding</text></g>
        <g transform="translate(0,508)"><circle cx="38" cy="-4" r="4.5" fill="var(--orange)"/><text x="48" y="0">Attic Ventilation</text></g>
        <g transform="translate(0,528)"><circle cx="38" cy="-4" r="4.5" fill="var(--orange)"/><text x="48" y="0">Gutters</text></g>
      </g>
      <text class="body-text" x="34" y="561" font-size="12.5" font-weight="700" fill="var(--orange)">CALL FOR A QUOTE TODAY.</text>
      <path d="M36 571 q-3 3 0 8 l5 5 q5 3 8 0 l-3 -3 -3 2 -5 -5 2 -3 z" fill="var(--orange)"/>
      <text class="body-text" x="53" y="583" font-size="17.5" font-weight="700" fill="var(--white)">716-555-0147</text>
    </g>

    <g class="headline">
      <text class="display" x="243" y="423" font-size="55" fill="var(--black)" textLength="266">RELIABILITY</text>
      <text class="heavy" x="243" y="445" font-size="22.5" fill="var(--white)">STARTS AT THE TOP</text>
      <text class="display" x="243" y="502" font-size="48" fill="var(--black)">WE OFFER</text>
      <text class="body-text" x="243" y="519" font-size="16" font-weight="700" fill="var(--white)">A 15 YEAR WARRANTY</text>
      <text class="body-text" x="243" y="534" font-size="13" fill="var(--white)">with our platinum roof program.</text>
      <text class="body-text" x="243" y="560" font-size="14.5" font-weight="700" fill="var(--white)">WE ARE CERTIFIED BY DWELLMATCH,</text>
      <text class="body-text" x="243" y="580" font-size="14.5" font-weight="700" fill="var(--white)">HARLAN TREVISK, QUARNO.</text>
    </g>

    <g class="project-photos">
      <rect x="20" y="610" width="168" height="106" fill="#6a6f78" role="img" aria-label="Photo of a house roof being stripped and re-shingled"/>
      <rect x="193" y="610" width="167" height="106" fill="#7f7c70" role="img" aria-label="Photo of a roofing delivery truck parked in a residential driveway"/>
      <rect x="365" y="610" width="168" height="106" fill="#8e7a66" role="img" aria-label="Photo of roofers working on exposed roof decking in winter"/>
    </g>

    <g class="footer body-text" font-size="10" font-weight="600" fill="var(--black)">
      <rect y="725" width="553" height="52" fill="var(--white)"/>
      <path d="M24 745 a4 4 0 1 1 8 0 q0 3 -4 9 q-4 -6 -4 -9 z" fill="var(--orange)"/>
      <text x="35" y="752">4187 Merrow Rd, Buffalo, NY 14215</text>
      <circle cx="222" cy="749" r="3.5" fill="none" stroke="var(--orange)" stroke-width="1.2"/>
      <text x="232" y="752">www.ktw-roofing.com</text>
      <text x="386" y="752" font-weight="700" fill="var(--orange)" font-size="11">Follow us:</text>
      <text x="438" y="752" font-size="9">linkpage</text>
      <text x="476" y="752" font-size="9">frunt</text>
      <text x="503" y="752" font-size="9">wexora</text>
    </g>
  </svg>

  <!-- Business card front -->
  <svg class="piece card-front" viewBox="0 0 542 310" xmlns="http://www.w3.org/2000/svg">
    <rect width="542" height="310" fill="var(--black)"/>
    <polygon points="0,0 70,0 281,310 0,310" fill="var(--orange)"/>
    <polygon points="0,143 0,178 90,310 118,310" fill="var(--black)"/>
    <polygon points="86,0 106,0 226,153 206,153" fill="var(--orange)"/>
    <polygon points="121,0 141,0 264,153 244,153" fill="var(--orange)"/>
    <rect x="335" y="148" width="18" height="18" fill="var(--orange)"/>
    <text class="brand" x="362" y="172" font-size="40" fill="var(--mark-gray)">KTW</text>
    <text class="tagline" x="390" y="199" font-size="15" fill="var(--orange)" text-anchor="middle">ROOFING-SIDING-STONE</text>
    <circle cx="324" cy="232" r="4" fill="none" stroke="var(--orange)" stroke-width="1.3"/>
    <text class="body-text" x="334" y="236" font-size="12.5" fill="var(--white)">www.ktw-roofing.com</text>
  </svg>

  <!-- Business card back -->
  <svg class="piece card-back" viewBox="0 0 542 310" xmlns="http://www.w3.org/2000/svg">
    <rect width="542" height="310" fill="var(--white)"/>
    <polygon points="170,118 542,118 542,310 317,310" fill="var(--black)"/>
    <polygon points="32,90 162,90 317,310 200,310" fill="var(--orange)"/>
    <polygon points="188,90 203,90 285,203 270,203" fill="var(--orange)"/>
    <polygon points="220,90 235,90 312,203 297,203" fill="var(--orange)"/>
    <rect x="330" y="66" width="15" height="15" fill="var(--orange)"/>
    <text class="brand" x="352" y="86" font-size="32" fill="var(--mark-gray)">KTW</text>
    <text class="tagline" x="380" y="106" font-size="12" fill="var(--orange)" text-anchor="middle">ROOFING-SIDING-STONE</text>
    <g class="contact body-text" fill="var(--white)">
      <path d="M311 177 q-3 3 0 7 l5 5 q4 3 7 0 l-3 -3 -3 2 -4 -5 2 -3 z" fill="var(--orange)"/>
      <text x="330" y="189" font-size="14" font-weight="700">716-555-0147</text>
      <path d="M311 203 a4 4 0 1 1 8 0 q0 3 -4 8 q-4 -5 -4 -8 z" fill="var(--orange)"/>
      <text x="325" y="210" font-size="12">4187 Merrow Rd, Buffalo, NY 14215</text>
      <circle cx="314" cy="226" r="3.5" fill="none" stroke="var(--orange)" stroke-width="1.2"/>
      <text x="325" y="229" font-size="12">www.ktw-roofing.com</text>
    </g>
    <text class="body-text" x="23" y="249" font-size="14" font-weight="700" fill="var(--orange)">Follow us:</text>
    <g class="body-text" font-size="12" font-weight="600" fill="var(--black)">
      <text x="23" y="271">linkpage</text>
      <text x="75" y="271">frunt</text>
      <text x="110" y="271">wexora</text>
    </g>
  </svg>

</main>
</body>
</html>
```